The Velvet Groove Company Brochure

I am the owner of a Mobile Disc Jockey company specializing in weddings. I am looking for a Tri Fold color brochure that is modern and eye catching with the focus being on upscale wedding events. I also want it to be easy to read and not overly cluttered ! I would like it to reflect our website located at thevelvetgroovehq.com
I also have different variations and file types of my logo such as jpeg and png files. I need some good dance floor pics. If you do not have any good stock photos I can look through my photo library. I uploaded a logo and pic I found from one of my videos. Not sure if it is worth anything.
We also do Uplighting and Photo Booths which I would like in the brochure. Much of the text copy needed can be taken from our website if needed. Please refer to the website to see what we do and our style.

Target Market(s)

upscale weddings

Industry/Entity Type

wedding dj entertainment & masters of ceremonies

Requirements
Nice to have
• nice pictures of packed dance floors and people having fun

```html
<!DOCTYPE html>
<html lang="en">
<head>
<meta charset="utf-8">
<title>The Velvet Groove – Tri-Fold Brochure</title>
<link rel="stylesheet" href="https://fonts.googleapis.com/css2?family=Poppins:wght@200;300;400;600;700&display=swap">
<style>
  :root{
    --purple:#7b2d91;
    --purple-light:#a45bbd;
    --purple-pale:#c99ad8;
    --ink:#1f1f1f;
    --grey:#6d6e71;
    --white:#ffffff;
    --stage:#e4e4e4;
  }
  *{box-sizing:border-box;margin:0;padding:0}
  html,body{width:864px;height:1200px;overflow:hidden;background:var(--stage)}
  body{font-family:"Poppins",sans-serif;color:var(--ink);position:relative}
  .spread{position:absolute;left:24px;width:816px;height:570px;background:var(--white);overflow:hidden;box-shadow:0 4px 14px rgba(0,0,0,.12)}
  .spread--outside{top:20px}
  .spread--inside{top:610px}
  .spread svg.shapes{position:absolute;inset:0}
  .block{position:absolute}
  .brand{display:flex;align-items:center;gap:6px;font-weight:600;color:var(--grey);letter-spacing:.2px}
  .brand__dot{width:14px;height:14px;border-radius:50%;background:var(--purple);flex:none}
  .brand--tab{left:16px;top:28px;background:var(--white);padding:8px 14px;border-radius:0 16px 16px 0;font-size:14px}
  .brand--cover{left:585px;top:26px;font-size:19px}
  .brand--inside{left:296px;top:300px;font-size:11px}
  .brand--inside .brand__dot{width:10px;height:10px}
  .body-copy{font-size:8.4px;line-height:1.5;font-weight:400}
  .body-copy p+p{margin-top:7px}
  /* outside */
  .flap-text{left:28px;top:302px;width:226px}
  .testimonial{font-size:11px;font-weight:700;line-height:1.25;text-transform:uppercase}
  .flap-heading{margin-top:9px;color:var(--purple);font-size:11px;font-weight:700;line-height:1.25;text-transform:uppercase}
  .flap-text .body-copy{margin-top:7px;font-size:8.2px}
  .contact{left:272px;top:82px;width:272px;text-align:center;color:var(--white)}
  .contact__label{font-size:12px;font-weight:600;text-transform:uppercase}
  .contact__phone{font-size:22px;font-weight:700;letter-spacing:.5px;line-height:1.1}
  .contact__tagline{margin-top:18px;font-size:11.5px;font-weight:700;line-height:1.3;text-transform:uppercase}
  .contact__web{margin-top:16px;font-size:9.5px;font-weight:600}
  .cover-text{left:560px;top:300px;width:240px;text-align:center;color:var(--white)}
  .cover-text__title{font-size:22px;font-weight:200;line-height:1.15;text-transform:uppercase;letter-spacing:.5px}
  .cover-text__sub{margin-top:12px;font-size:9.5px;font-weight:600;line-height:1.4}
  .cover-text__web{margin-top:10px;font-size:9.5px;font-weight:600}
  /* inside */
  .section-title{font-size:14px;font-weight:700;text-transform:uppercase;color:var(--purple)}
  .weddings{left:20px;top:20px;width:245px;color:var(--white)}
  .weddings .section-title{color:var(--white)}
  .weddings__sub{margin-top:6px;font-size:10px;font-weight:600;line-height:1.3}
  .weddings .body-copy{margin-top:6px;color:#f3e6f7}
  .corporate{left:296px;top:18px;width:220px}
  .corporate .body-copy{margin-top:6px}
  .photobooth{left:574px;top:276px;width:226px}
  .photobooth .body-copy{margin-top:6px}
</style>
</head>
<body>

<section class="spread spread--outside">
  <svg class="shapes" width="816" height="570" viewBox="0 0 816 570">
    <defs>
      <linearGradient id="dancefloor" x1="0" y1="0" x2="0" y2="1">
        <stop offset="0" stop-color="#c86a7a"/>
        <stop offset=".5" stop-color="#8a5a8f"/>
        <stop offset="1" stop-color="#4a3a6a"/>
      </linearGradient>
      <linearGradient id="fogroom" x1="0" y1="0" x2="0" y2="1">
        <stop offset="0" stop-color="#b77ccc"/>
        <stop offset="1" stop-color="#8e4aa6"/>
      </linearGradient>
      <linearGradient id="couplefill" x1="0" y1="0" x2="1" y2="1">
        <stop offset="0" stop-color="#d9a66a"/>
        <stop offset="1" stop-color="#7a5236"/>
      </linearGradient>
    </defs>
    <path class="back-panel" d="M272,0 H544 V570 H330 C300,450 285,300 272,210 Z" fill="var(--purple)"/>
    <path d="M0,558 L272,542 L272,570 L0,570 Z" fill="var(--purple)"/>
    <path d="M40,0 H250 V205 C250,262 212,292 160,292 H100 C66,292 40,266 40,232 Z" fill="url(#dancefloor)" role="img" aria-label="Photo of a packed dance floor with guests hugging and celebrating"/>
    <rect x="600" y="78" width="170" height="170" rx="60" fill="url(#couplefill)" role="img" aria-label="Cutout of a couple dancing, filled with a reception photo"/>
    <path d="M420,570 C450,420 520,300 620,268 C700,244 760,238 816,222 V570 Z" fill="url(#fogroom)" role="img" aria-label="Wedding couple's first dance on a fog-covered floor under purple uplighting"/>
    <path d="M420,570 C450,420 520,300 620,268 C700,244 760,238 816,222" fill="none" stroke="var(--white)" stroke-width="4"/>
  </svg>

  <div class="block brand brand--tab"><span class="brand__dot"></span>The Velvet Groove</div>

  <div class="block flap-text">
    <p class="testimonial">Fantastic experience, highly recommend! – Danielle</p>
    <h2 class="flap-heading">The most recommended DJ's in Southwest Florida</h2>
    <div class="body-copy">
      <p>Our award winning DJs are recommended by the finest venues in Naples, Fort Myers and the surrounding areas and we are known for helping our clients create the ultimate wedding entertainment experience.</p>
      <p>We offer creative ideas and a fresh approach to help you customize your event around the style &amp; vibe that you want. Planning this way is fun and eliminates the stress that comes with preparing for your special day.</p>
    </div>
  </div>

  <div class="block contact">
    <p class="contact__label">Call us today</p>
    <p class="contact__phone">(555) 014-2290</p>
    <p class="contact__tagline">It's your day. Let us help<br>you make it happen,<br>your way</p>
    <p class="contact__web">www.thevelvetgroovehq.com</p>
  </div>

  <div class="block brand brand--cover"><span class="brand__dot"></span>The Velvet Groove</div>

  <div class="block cover-text">
    <h1 class="cover-text__title">Modern,<br>Tasteful, &amp; Fun<br>Entertainment</h1>
    <p class="cover-text__sub">Weddings, Corporate Events,<br>Private Parties, any event is better<br>with The Velvet Groove</p>
    <p class="cover-text__web">www.thevelvetgroovehq.com</p>
  </div>
</section>

<section class="spread spread--inside">
  <svg class="shapes" width="816" height="570" viewBox="0 0 816 570">
    <defs>
      <linearGradient id="partycrowd" x1="0" y1="0" x2="0" y2="1">
        <stop offset="0" stop-color="#9a3fae"/>
        <stop offset="1" stop-color="#3a2547"/>
      </linearGradient>
      <linearGradient id="singers" x1="0" y1="0" x2="1" y2="0">
        <stop offset="0" stop-color="#3d4f7a"/>
        <stop offset=".6" stop-color="#d7a98e"/>
        <stop offset="1" stop-color="#8c9fc0"/>
      </linearGradient>
      <linearGradient id="sendoff" x1="0" y1="0" x2="0" y2="1">
        <stop offset="0" stop-color="#3a2e2a"/>
        <stop offset="1" stop-color="#7a5b4a"/>
      </linearGradient>
    </defs>
    <path d="M0,0 H285 V215 C285,270 240,292 180,296 L0,306 Z" fill="var(--purple)"/>
    <path d="M0,330 L170,320 C230,315 275,290 290,260 V570 H0 Z" fill="url(#partycrowd)" role="img" aria-label="Guests dancing at a party under purple and blue lights"/>
    <circle cx="150" cy="350" r="60" fill="#b06ac6" stroke="var(--white)" stroke-width="4" role="img" aria-label="Close-up of a guest dancing"/>
    <path d="M520,0 H816 V95 C750,125 680,150 590,150 C550,150 525,120 520,90 Z" fill="url(#singers)" role="img" aria-label="Friends singing karaoke together into a microphone"/>
    <path d="M560,165 C660,165 740,140 816,110" fill="none" stroke="var(--purple)" stroke-width="4"/>
    <path d="M300,570 L300,420 C320,362 400,330 470,326 L560,326 L560,570 Z" fill="url(#sendoff)" role="img" aria-label="Bride and groom walking out through a confetti send-off"/>
    <circle cx="704" cy="205" r="52" fill="#6f6a80" stroke="var(--white)" stroke-width="4" role="img" aria-label="Guests posing with props in a photo booth"/>
  </svg>

  <div class="block weddings">
    <h2 class="section-title">Weddings</h2>
    <p class="weddings__sub">How do you want your wedding remembered?</p>
    <div class="body-copy">
      <p>This is one of the first questions I ask couples when they contact us about wedding DJ entertainment and the response is always the same,</p>
      <p>"I want a great party and everyone to leave saying it was the best wedding ever"!</p>
      <p>Beginning with your initial consultation, we listen to you and respond with creative ideas and helpful advice so your event is all about you. We know it's more than just great music, it's keeping you guests engaged and coordinating with your venue and vendors for a smooth and timely event everyone will never forget.</p>
    </div>
  </div>

  <div class="block corporate">
    <h2 class="section-title">Corporate</h2>
    <div class="body-copy">
      <p>With over 30+ years of experience providing DJ entertainment and lighting services for corporate events and company parties, we understand how important creating the right atmosphere and delivering quality entertainment is to the success of your event. So whether you're planning a sales incentive meeting, awards presentation, beach party, holiday party or gala evening, let us help you create an event your employees will never forget.</p>
      <p>Our DJs are always ready to fill your dance floor so everyone can cut loose and enjoy a well-deserved break. If you would rather a more reserved approach, we can also provide a non-interactive style as well!</p>
      <p>We offer Monogram branding services, Photobooths and engaging interactive entertainment such as Karaoke and game show entertainment!</p>
    </div>
  </div>

  <div class="block brand brand--inside"><span class="brand__dot"></span>The Velvet Groove</div>

  <div class="block photobooth">
    <h2 class="section-title">Photo Booth</h2>
    <div class="body-copy">
      <p>It's no secret photo booths have been a hit at weddings as well as any other event. Our photo booth offers a modern sleek look and is so simple to operate it doesn't need an attendant. However we want you and your guests to have the best experience possible so we provide one as part of our package.</p>
      <p>The combination of the right props and a fun and friendly attendant will even arouse the curiosity of your shyest guests. Once they leave the photo booth they head to the dance floor to continue the fun.</p>
    </div>
  </div>
</section>

</body>
</html>
```